Vorna Fleet business card

I am needing a business card that at a glance shows all the services that we provide emphasizing some more than others. We are a Fleet and Compliance management company as well as a software company. We provide outsourced solutions for KPX compliance and HR services via our own software.
In addition, we do
drug testing
GPS
Cameras
Electronic DVIRS
ELD's

Target Market(s)

Transportation company owners

Industry/Entity Type

Transportation supplier

Contact Information for Business Card

the card should inform potential customers what we do

Other font styles liked:
• I have added brand guidelines. See attached

Requirements
Must have
• See description
Should not have
• Colors outside my brand guide. See attached

```html
<!DOCTYPE html>
<html lang="en">
<head>
<meta charset="utf-8">
<title>Vorna Fleet business card</title>
<link href="https://fonts.googleapis.com/css2?family=Arimo:wght@400;700&family=Raleway:wght@700&display=swap" rel="stylesheet">
<style>
  :root {
    --brand-red: #ee2431;
    --brand-black: #0b0b0b;
    --paper: #ffffff;
    --stage: #d9d9d9;
    --rule: #d4d4d4;
    --ghost: #ececec;
    --ink: #1a1a1a;
  }
  * { box-sizing: border-box; margin: 0; padding: 0; }
  html, body { width: 1200px; height: 900px; overflow: hidden; }
  body {
    background: var(--stage);
    font-family: "Arimo", Arial, sans-serif;
    color: var(--ink);
    position: relative;
  }
  .card {
    position: absolute;
    left: 276px;
    width: 648px;
    height: 370px;
    background: var(--paper);
    box-shadow: 0 6px 14px rgba(0,0,0,.25);
    overflow: hidden;
  }
  .card--front { top: 50px; }
  .card--back { top: 470px; }

  /* front */
  .front__brand {
    height: 180px;
    display: flex;
    align-items: center;
    justify-content: center;
    gap: 16px;
  }
  .brand-mark {
    width: 30px; height: 30px;
    background: var(--brand-red);
  }
  .brand-name {
    font-family: "Arimo", Arial, sans-serif;
    font-weight: 700;
    color: var(--brand-black);
    font-size: 58px;
    letter-spacing: 1px;
    line-height: 1;
  }
  .front__band {
    height: 190px;
    background: var(--brand-black);
    color: var(--paper);
    text-align: center;
    padding-top: 28px;
  }
  .front__headline {
    font-size: 23px;
    line-height: 1.25;
    letter-spacing: .5px;
    text-transform: uppercase;
  }
  .front__lead {
    color: var(--brand-red);
    font-size: 16px;
    margin-top: 14px;
  }
  .front__services {
    font-size: 16px;
    line-height: 1.3;
    margin-top: 2px;
  }

  /* back */
  .back__brand {
    position: absolute;
    left: 44px; top: 56px;
    display: flex; align-items: center; gap: 14px;
  }
  .back__brand .brand-name { font-size: 50px; }
  .back__ghost {
    position: absolute;
    right: 24px; top: 180px;
    font-weight: 700;
    font-size: 92px;
    color: var(--ghost);
    line-height: 1;
  }
  .person {
    position: absolute;
    right: 44px; top: 76px;
    text-align: right;
  }
  .person__name {
    font-family: "Raleway", Arial, sans-serif;
    font-weight: 700;
    color: var(--brand-red);
    font-size: 27px;
  }
  .person__role {
    font-size: 14px;
    color: #444;
    margin-top: 2px;
    padding-top: 3px;
    border-top: 1px solid var(--rule);
    display: inline-block;
    padding-left: 40px;
  }
  .back__rule {
    position: absolute;
    left: 44px; right: 44px; top: 196px;
    border-top: 1px solid var(--rule);
  }
  .contacts {
    position: absolute;
    left: 52px; top: 234px;
    list-style: none;
  }
  .contacts li {
    display: flex; align-items: center; gap: 18px;
    font-size: 18px;
    height: 32px;
  }
  .contacts svg { width: 16px; height: 16px; fill: var(--brand-red); }
  .back__edge {
    position: absolute;
    left: 0; right: 0; bottom: 0;
    height: 10px;
    background: var(--brand-red);
  }
</style>
</head>
<body>
  <section class="card card--front">
    <div class="front__brand">
      <span class="brand-mark"></span>
      <span class="brand-name">Vorna Fleet</span>
    </div>
    <div class="front__band">
      <p class="front__headline">Outsourced solutions for<br>KPX compliance and HR services</p>
      <p class="front__lead">In addition, we do:</p>
      <p class="front__services">Drug Testing &nbsp;- &nbsp;GPS &nbsp;- &nbsp;Cameras<br>Electronic DVIRS &nbsp;- &nbsp;ELD's</p>
    </div>
  </section>

  <section class="card card--back">
    <div class="back__brand">
      <span class="brand-mark"></span>
      <span class="brand-name">Vorna Fleet</span>
    </div>
    <span class="back__ghost" aria-hidden="true">Vorna</span>
    <div class="person">
      <p class="person__name">Mara Ostell</p>
      <p class="person__role">Director</p>
    </div>
    <div class="back__rule"></div>
    <ul class="contacts">
      <li>
        <svg viewBox="0 0 24 24" aria-hidden="true"><path d="M6.6 10.8a15 15 0 0 0 6.6 6.6l2.2-2.2a1 1 0 0 1 1-.25 11.4 11.4 0 0 0 3.6.57 1 1 0 0 1 1 1V20a1 1 0 0 1-1 1A17 17 0 0 1 3 4a1 1 0 0 1 1-1h3.5a1 1 0 0 1 1 1c0 1.25.2 2.45.57 3.57a1 1 0 0 1-.25 1z"/></svg>
        (480) 555 0182
      </li>
      <li>
        <svg viewBox="0 0 24 24" aria-hidden="true"><path d="M2 5h20v14H2z M2 5l10 8 10-8" fill="none" stroke="#ee2431" stroke-width="2.5"/></svg>
        info@vornafleet.com
      </li>
      <li>
        <svg viewBox="0 0 24 24" aria-hidden="true"><circle cx="12" cy="12" r="10"/><path d="M2 12h20M12 2c3 3 3 17 0 20M12 2c-3 3-3 17 0 20" stroke="#fff" stroke-width="1.5" fill="none"/></svg>
        www.vornafleet.com
      </li>
    </ul>
    <div class="back__edge"></div>
  </section>
</body>
</html>
```